/ custom plush toys for luxury hotel /

We are, a US company that makes custom plush toys for luxury hotels only. (our customers)
our logo is a mascot:
a teddy bear dressing up as a hotel concierge, the message is: in terms of teddy bear we are your concierge
These plushies are intended to be offered to the children of the customers of these luxurious hotels.
To convince our customers who will land on this site to contact us and work with us, we want to convey the message that our client (the hotel) will make HIS client and HIS children happy by offering them an unexpected gift at the check-in , also to make understand that it is very powerful advertising and marketing object for the hotel (this plush and its LOGO obviously will accompany the children of these customers everywhere).
We also want to insist on the fact that our solution is turnkey, starting from your wishes we take care of everything from the creation of the design to the delivery of the finished products, you do not worry about anything else.
Here is our process:
We only do custom, the customer gives us his theme and ideas and from that we propose different designs, drawing, 3D visualizations, once the design is approved, we make a physical sample that we have validated or modified by our client...
We would like to have a website/landing page to present our concept and our company, also to involve our future customers to contact us by mail or phone, this should be the objective of this page
We want to use themes like teddy bear, luxury, , kids, custom made, handmade, hand drawing..
We really want to emphasize the customization: we create your teddy bear from scratch.
We do not have a catalog because made-to-measure and therefore really want to involve our future customers to contact us by mail.
I can provide you with some of this content (sources file available):
Our Logo
Pictures of some plushies that we made this year
Drawings,
3D
a brief comic strip that we made to present us
Here are some examples attached .
also: Some content that I don't have but that I think would fit in the thematic:
happy children with a teddy bear /
the steps of manufacturing (a seamstress? / the selection of a fabric?) / a designer at work on a drawing board /
etc
Waiting for your proposal,
available if precisions needed
Thank you for your time
Tobi
Luxury Hotel Manager / Purchaser

```html
<!DOCTYPE html>
<html lang="en">
<head>
<meta charset="utf-8">
<title>Plushcourt — Soft Toys For Luxury Hotels</title>
<link href="https://fonts.googleapis.com/css2?family=Poppins:wght@400;500;600;700;800&display=swap" rel="stylesheet">
<style>
:root{
  --navy:#231f57;
  --navy-deep:#2a2668;
  --ink:#1d1a45;
  --text:#55536b;
  --orange:#ff8a5b;
  --peach:#ffa36c;
  --sun:#ffd27c;
  --cream:#fff6da;
  --grey:#efefef;
  --card:#e6e6e8;
  --white:#ffffff;
}
*{box-sizing:border-box;margin:0;padding:0}
html,body{width:1200px;height:4259px;overflow:hidden}
body{position:relative;background:var(--white);font-family:"Poppins",sans-serif;color:var(--text)}
.abs{position:absolute}
.ph{position:absolute;border-radius:24px}
h1,h2,h3{font-family:"Poppins",sans-serif;color:var(--ink);font-weight:800}
.btn{position:absolute;display:flex;align-items:center;justify-content:center;border-radius:30px;font-weight:700;font-size:12px;text-transform:uppercase;letter-spacing:.3px}
.btn-orange{background:linear-gradient(90deg,#ff8a5b,#ffb37a);color:#fff;box-shadow:0 6px 16px rgba(255,138,91,.35)}
.btn-white{background:#fff;color:var(--ink)}

/* hero */
.hero-bg{left:0;top:0;width:1200px;height:740px}
.brand{left:86px;top:22px;display:flex;align-items:center;gap:10px}
.brand-dot{width:28px;height:28px;border-radius:50%;background:var(--orange)}
.brand-name{font-size:24px;font-weight:700;color:var(--orange)}
.nav{left:456px;top:46px;display:flex;gap:28px;font-size:12px;font-weight:500;color:var(--ink)}
.nav .active{font-weight:700}
.join{left:988px;top:34px;width:122px;height:44px}
.hero-title{left:84px;top:244px;font-size:72px;line-height:80px}
.hero-sub{left:86px;top:496px;font-size:15px;color:var(--ink)}
.cool{left:338px;top:168px;width:82px;height:46px;border-radius:24px;background:var(--peach);color:#fff;font-weight:700;font-size:17px;display:flex;align-items:center;justify-content:center;transform:rotate(-18deg)}

/* about */
.about-title{left:566px;top:818px;font-size:40px;line-height:46px}
.about-copy{left:566px;top:924px;width:460px;font-size:13.5px;line-height:25px}
.about-copy p+p{margin-top:18px}
.choose1{left:566px;top:1148px;width:122px;height:42px}

.stat{position:absolute;top:1290px;width:245px;height:336px;background:#fff;border-radius:22px;box-shadow:0 14px 30px rgba(0,0,0,.08)}
.stat .ph{left:10px;top:10px;width:225px;height:178px;border-radius:16px}
.stat .num{position:absolute;top:196px;width:100%;text-align:center;font-size:44px;font-weight:800;color:var(--navy)}
.stat .lbl{position:absolute;top:244px;width:100%;text-align:center;font-size:16px;color:var(--ink)}
.stat .go{position:absolute;right:14px;bottom:18px;width:52px;height:52px;border-radius:50%;background:var(--navy);display:flex;align-items:center;justify-content:center}

.why-title{left:232px;top:1842px;font-size:40px;line-height:44px;color:#fff}
.why-copy{left:232px;top:1942px;width:430px;font-size:13px;line-height:22px;color:#fff}
.choose2{left:230px;top:2046px;width:122px;height:42px}

/* design */
.sec-title{position:absolute;left:0;width:1200px;text-align:center;font-size:40px}
.feat{position:absolute;width:330px}
.feat h3{font-size:18px;font-weight:700}
.feat p{font-size:13px;line-height:20px;margin-top:6px}
.feat .ic{position:absolute;top:0;width:58px;height:62px;border-radius:12px;background:#ffe3cf}
.feat.l{text-align:right}
.feat.l .ic{right:-76px}
.feat.r .ic{left:-84px}
.divider{left:88px;top:2726px;width:1024px;height:1px;background:#e4e4e4}

.gal{position:absolute;top:2864px;width:196px;height:240px;border-radius:16px}
.arrow{position:absolute;top:3134px;width:52px;height:52px;border-radius:50%;display:flex;align-items:center;justify-content:center}

.contact-ghost{left:0;top:3208px;width:1200px;text-align:center;font-size:200px;font-weight:800;color:#f0f0f2;letter-spacing:4px;line-height:200px}
.touch{left:0;top:3390px;width:1200px;text-align:center;font-size:40px}
.touch-btn{left:530px;top:3464px;width:140px;height:42px}

/* newsletter */
.news{left:139px;top:3584px;width:922px;height:206px;border-radius:103px;background:linear-gradient(90deg,#ff8d62,#ffb978 55%,#ffd27c)}
.news h2{position:absolute;left:78px;top:42px;font-size:40px;line-height:48px;color:#fff}
.news small{position:absolute;left:78px;top:144px;font-size:12.5px;color:#fff}
.email{position:absolute;left:488px;top:74px;width:386px;height:58px;border-radius:30px;background:#fff;display:flex;align-items:center;padding-left:24px;font-size:13px;color:#8a889a;gap:12px}
.email .send{position:absolute;right:8px;top:8px;width:42px;height:42px;border-radius:50%;background:var(--navy);display:flex;align-items:center;justify-content:center}

/* footer */
.foot-col{position:absolute;top:3940px;color:#fff}
.foot-col h4{font-size:19px;font-weight:700;margin-bottom:18px}
.foot-col li{list-style:none;font-size:12.5px;line-height:31px;color:#e5e4f4}
.foot-col li::before{content:"› ";}
.foot-col.info li{line-height:20px;margin-bottom:14px}
.foot-col.info li::before{content:""}
.social{position:absolute;top:4002px;width:50px;height:50px;border-radius:50%;background:rgba(255,255,255,.14)}
.foot-line{left:88px;top:4196px;width:1024px;height:1px;background:rgba(255,255,255,.18)}
.copy{left:0;top:4220px;width:1200px;text-align:center;font-size:13px;font-weight:600;color:#fff}
.totop{left:1126px;top:4166px;width:42px;height:42px;border-radius:50%;background:var(--orange);display:flex;align-items:center;justify-content:center}
</style>
</head>
<body>

<!-- hero -->
<svg class="abs hero-bg" viewBox="0 0 1200 740" aria-hidden="true">
  <defs><linearGradient id="heroGrey" x1="0" y1="0" x2="0" y2="1"><stop offset="0" stop-color="#f2f2f2"/><stop offset="1" stop-color="#e9e9ea"/></linearGradient></defs>
  <path d="M0 0H1200V490C1100 470 1010 520 900 600C800 660 720 630 640 660C560 690 470 740 380 712C300 690 240 620 130 620C70 620 30 600 0 580Z" fill="url(#heroGrey)"/>
</svg>
<div class="abs brand"><span class="brand-dot"></span><span class="brand-name">Plushcourt</span></div>
<nav class="abs nav">
  <span class="active">HOME</span><span>ABOUT</span><span>COLLECTIONS</span><span>GALLERY</span><span>REVIEWS</span><span>CONTACT US</span>
</nav>
<div class="btn btn-orange join">&#9679;&nbsp; Join Us</div>
<div class="abs cool">Cool</div>
<h1 class="abs hero-title">Soft Toys<br>For Luxury<br>Hotels</h1>
<p class="abs hero-sub">A teddy bear dressing up as a hotel concierge</p>
<div class="ph" role="img" aria-label="Pink plush handbag with paw print" style="left:524px;top:156px;width:376px;height:398px;background:linear-gradient(160deg,#f7b8cd,#ee9bb6)"></div>
<div class="ph" role="img" aria-label="Plush puppy with bow sitting upright" style="left:920px;top:190px;width:208px;height:364px;background:linear-gradient(160deg,#f8c184,#f1a054)"></div>

<!-- about -->
<svg class="abs" style="left:0;top:760px" width="1200" height="700" viewBox="0 0 1200 700" aria-hidden="true">
  <defs><linearGradient id="sunBlob" x1="0" y1="0" x2="0" y2="1"><stop offset="0" stop-color="#ffd27c"/><stop offset="1" stop-color="#fff6da" stop-opacity=".2"/></linearGradient>
  <linearGradient id="peachBlob" x1="0" y1="0" x2="1" y2="1"><stop offset="0" stop-color="#ffe0c8"/><stop offset="1" stop-color="#ff9a6a"/></linearGradient></defs>
  <path d="M110 220C160 160 300 150 350 240C390 320 380 480 330 600C240 700 90 690 40 560C0 450 60 280 110 220Z" fill="url(#sunBlob)" opacity=".8"/>
  <path d="M1060 60C1120 40 1200 40 1200 40V240C1140 260 1070 240 1060 180C1055 130 1040 80 1060 60Z" fill="url(#peachBlob)"/>
</svg>
<div class="ph" role="img" aria-label="Mascot bear in concierge uniform waving" style="left:238px;top:766px;width:268px;height:418px;background:linear-gradient(160deg,#b56a3a,#2d2a6e)"></div>
<div class="ph" role="img" aria-label="Green plush parrot" style="left:976px;top:694px;width:224px;height:186px;background:linear-gradient(160deg,#3fae4a,#2a8bbf)"></div>
<h2 class="abs about-title">What is<br>Plushcourt</h2>
<div class="abs about-copy">
  <p>Aenean sollicitudin, lorem quis bibendum auctor, nisi elit consequat ipsum, nec sagittis sem nibh id elit. Duis sed odio sit amet nibh vulputate cursus a sit amet mauris. Morbi accumsan ipsum velit nam nec tellus a odio tincidunt.</p>
  <p>Auctor a ornare odio Sed non mauris vitae erat consequat auctor eu in elit. Class aptent taciti sociosqu ad litora torquent sagittis sem nibh id elit.</p>
</div>
<div class="btn btn-orange choose1">Choose Us</div>

<!-- wave band -->
<svg class="abs" style="left:0;top:1520px" width="1200" height="780" viewBox="0 0 1200 780" aria-hidden="true">
  <defs><linearGradient id="band" x1="0" y1="0" x2="1" y2="0"><stop offset="0" stop-color="#ff7f55"/><stop offset=".55" stop-color="#ffae74"/><stop offset="1" stop-color="#ffd27c"/></linearGradient></defs>
  <path d="M0 270C180 270 320 270 470 200C620 130 700 60 880 80C1040 100 1150 160 1200 200V640C1080 700 960 700 860 660C760 620 680 640 560 680C420 720 260 720 120 680C60 660 20 640 0 630Z" fill="url(#band)"/>
  <path d="M0 320C80 320 120 420 100 520C90 600 50 690 0 670Z" fill="#ff7040" opacity=".5"/>
  <path d="M0 690C200 740 400 720 560 690" stroke="#ffd6c4" stroke-width="3" fill="none" opacity=".7"/>
</svg>

<div class="stat" style="left:210px"><div class="ph" role="img" aria-label="Plush bulldog with red scarf" style="background:linear-gradient(160deg,#e3e3e5,#d7c2a4)"></div><div class="num">05</div><div class="lbl">Collections</div><div class="go"><svg width="14" height="14" viewBox="0 0 14 14"><path d="M5 3l4 4-4 4" stroke="#fff" stroke-width="2" fill="none"/></svg></div></div>
<div class="stat" style="left:478px"><div class="ph" role="img" aria-label="Plush sea turtle" style="background:linear-gradient(160deg,#e3e3e5,#7fa36e)"></div><div class="num">25</div><div class="lbl">Artists</div><div class="go"><svg width="14" height="14" viewBox="0 0 14 14"><path d="M5 3l4 4-4 4" stroke="#fff" stroke-width="2" fill="none"/></svg></div></div>
<div class="stat" style="left:746px"><div class="ph" role="img" aria-label="Plush tropical fish" style="background:linear-gradient(160deg,#e3e3e5,#6f8c9c)"></div><div class="num">250</div><div class="lbl">Items</div><div class="go"><svg width="14" height="14" viewBox="0 0 14 14"><path d="M5 3l4 4-4 4" stroke="#fff" stroke-width="2" fill="none"/></svg></div></div>

<h2 class="abs why-title">Why Are They So<br>Exclusive</h2>
<p class="abs why-copy">Aenean sollicitudin, lorem quis bibendum auctor, nisi elit consequat ipsum, nec sagittis sem nibh id elit. Duis sed odio sit amet nibh vulputate cursus a sit amet mauris. Morbi accumsan ipsum velit. Nam nec tellus a odio tincidun...</p>
<div class="btn btn-white choose2">Choose Us</div>
<div class="ph" role="img" aria-label="Black plush bulldog with red scarf" style="left:700px;top:1750px;width:330px;height:430px;background:linear-gradient(160deg,#4a4a52,#2b2b30)"></div>

<!-- design -->
<h2 class="sec-title" style="top:2266px">Stuffed Toys Design</h2>
<div class="feat l" style="left:80px;top:2350px"><div class="ic" role="img" aria-label="Teddy bear icon"></div><h3>Teddy bear</h3><p>Lorem quis bibendum auctor nisi elit<br>consequat ipsum nec sagittis</p></div>
<div class="feat l" style="left:80px;top:2455px"><div class="ic" role="img" aria-label="Hotel building icon"></div><h3>Luxury</h3><p>Lorem quis bibendum auctor nisi elit<br>consequat ipsum nec sagittis</p></div>
<div class="feat l" style="left:80px;top:2568px"><div class="ic" role="img" aria-label="Children icon"></div><h3>Kids</h3><p>Lorem quis bibendum auctor nisi<br>elit consequat ipsum nec sagittis</p></div>
<div class="feat r" style="left:868px;top:2350px"><div class="ic" role="img" aria-label="Tools icon"></div><h3>Custom made</h3><p>Lorem quis bibendum auctor nisi elit<br>consequat ipsum nec sagittis</p></div>
<div class="feat r" style="left:868px;top:2455px"><div class="ic" role="img" aria-label="Hands with heart icon"></div><h3>Handmade</h3><p>Lorem quis bibendum auctor nisi elit<br>consequat ipsum nec sagittis</p></div>
<div class="feat r" style="left:868px;top:2568px"><div class="ic" role="img" aria-label="Drawing board icon"></div><h3>Hand drawing</h3><p>Lorem quis bibendum auctor nisi elit<br>consequat ipsum nec sagittis</p></div>
<svg class="abs" style="left:447px;top:2354px" width="290" height="290" viewBox="0 0 290 290" aria-hidden="true">
  <circle cx="145" cy="145" r="143" fill="#fff" stroke="#ffb67a" stroke-width="4"/>
  <circle cx="145" cy="145" r="128" fill="#ffc978"/>
</svg>
<div class="ph" role="img" aria-label="Mascot bear in concierge uniform" style="left:476px;top:2354px;width:232px;height:282px;border-radius:50% 50% 40% 40%;background:linear-gradient(160deg,#b56a3a,#2d2a6e);opacity:.9"></div>
<div class="abs divider"></div>

<!-- gallery -->
<svg class="abs" style="left:740px;top:2940px" width="460" height="420" viewBox="0 0 460 420" aria-hidden="true">
  <path d="M120 60C220 0 400 20 460 60V420H60C0 360 20 140 120 60Z" fill="#fff6da"/>
</svg>
<h2 class="sec-title" style="top:2780px">Our Gallery</h2>
<div class="gal" role="img" aria-label="Black plush bulldog" style="left:88px;background:linear-gradient(160deg,#e6e6e8,#45454d)"></div>
<div class="gal" role="img" aria-label="Plush puppy with bow" style="left:295px;background:linear-gradient(160deg,#e6e6e8,#f3b06a)"></div>
<div class="gal" role="img" aria-label="Plush bulldog with red scarf" style="left:502px;background:linear-gradient(160deg,#e6e6e8,#cdb08e)"></div>
<div class="gal" role="img" aria-label="Plush tropical fish" style="left:708px;background:linear-gradient(160deg,#e6e6e8,#6f8c9c)"></div>
<div class="gal" role="img" aria-label="Green plush parrot" style="left:914px;background:linear-gradient(160deg,#e6e6e8,#3fae4a)"></div>
<div class="arrow" style="left:542px;background:linear-gradient(135deg,#ff8a5b,#ffc27a)"><svg width="14" height="14" viewBox="0 0 14 14"><path d="M9 3L5 7l4 4" stroke="#fff" stroke-width="2" fill="none"/></svg></div>
<div class="arrow" style="left:606px;background:var(--navy)"><svg width="14" height="14" viewBox="0 0 14 14"><path d="M5 3l4 4-4 4" stroke="#fff" stroke-width="2" fill="none"/></svg></div>

<!-- contact -->
<div class="abs contact-ghost">Contact</div>
<div class="ph" role="img" aria-label="Plush bulldog with red scarf" style="left:252px;top:3340px;width:112px;height:160px;background:linear-gradient(160deg,#d8c4a4,#b38f67)"></div>
<h2 class="abs touch">Get In Touch With Us</h2>
<div class="btn btn-orange touch-btn">Contact Us</div>

<!-- footer background -->
<svg class="abs" style="left:0;top:3640px" width="1200" height="619" viewBox="0 0 1200 619" aria-hidden="true">
  <path d="M0 80C120 160 260 250 400 240C560 230 700 190 860 150C980 120 1080 30 1200 60V619H0Z" fill="var(--navy-deep)"/>
  <path d="M880 250C960 210 1060 230 1080 300C1100 370 1020 410 950 390C880 370 830 290 880 250Z" fill="#34307a" opacity=".7"/>
</svg>

<!-- newsletter -->
<section class="abs news">
  <h2>Stay Up To Date<br>With Newsletter</h2>
  <small>Subscribe to our email address to get the latest news.</small>
  <div class="email">
    <svg width="16" height="12" viewBox="0 0 16 12"><rect x="1" y="1" width="14" height="10" rx="1" fill="none" stroke="#b8b6c6" stroke-width="1.4"/><path d="M1 1l7 6 7-6" fill="none" stroke="#b8b6c6" stroke-width="1.4"/></svg>
    Enter your email address...
    <div class="send"><svg width="16" height="16" viewBox="0 0 16 16"><path d="M2 8L14 2 11 14 8 9Z" fill="#fff"/></svg></div>
  </div>
</section>

<!-- footer -->
<div class="abs" style="left:100px;top:3950px;display:flex;align-items:center;gap:10px">
  <span class="brand-dot" style="width:34px;height:34px"></span><span class="brand-name" style="font-size:26px">Plushcourt</span>
</div>
<div class="foot-col" style="left:332px"><h4>Quick links</h4><ul><li>About Us</li><li>Collections</li><li>Gallery</li><li>Reviews</li><li>Contact Us</li></ul></div>
<div class="foot-col" style="left:508px"><h4>Information</h4><ul><li>Privacy Policy</li><li>Terms &amp; Conditions</li><li>FAQ's</li><li>Sitemap</li><li>Blog</li></ul></div>
<div class="foot-col info" style="left:716px"><h4>Contact info</h4><ul>
  <li>&#9993; Email:<br>&nbsp;&nbsp;&nbsp;&nbsp;info@example.com</li>
  <li>&#9742; Phone:<br>&nbsp;&nbsp;&nbsp;&nbsp;+08 123 456 7890</li>
  <li>&#9906; Location:<br>&nbsp;&nbsp;&nbsp;&nbsp;Some address line here<br>&nbsp;&nbsp;&nbsp;&nbsp;United Kingdom</li>
</ul></div>
<div class="social" style="left:940px" role="img" aria-label="Social profile link"></div>
<div class="social" style="left:1000px" role="img" aria-label="Social profile link"></div>
<div class="social" style="left:1060px" role="img" aria-label="Social profile link"></div>
<div class="abs totop"><svg width="14" height="14" viewBox="0 0 14 14"><path d="M7 12V3M3 7l4-4 4 4" stroke="#fff" stroke-width="1.8" fill="none"/></svg></div>
<div class="abs foot-line"></div>
<p class="abs copy">© Copyright 2022 , All Rights Reserved</p>

</body>
</html>
```